QLV Fashion Design Company Needs a New Web Design, Please Click Me

Designers:

PLEASE NOTE: we only need the web page design, not a fully coded website.

Our brand's name is The Bright Quarry, our signature is print. our style is edgy and chic.

The old website is too messy. here's the address:
www.qlvstudio.com.cn

The new website's purpose is to show our brand/design and most importantly, sell products, So it should be a combination of a designer official website and online shopping. I want the whole style to be clean, edgy and pioneer, easy to understand. we need a sophisticated online shopping website.

The reference websites are:
merolatest.co.uk
www.pd-kor.com
lucasvemm.com
orbaduvi.com
talumerosapkin.com

Please beat their designs :)

Check out our lasted fashion show to get to know us more.

https://www.vidplexa.com/watch?v=ZkamWtrBnoLe&spfreload=10

The attachments are our Logo and some 2015 Look Book.
(Please let us know if you want to play with our print in this particular web design, we can send the source file.)
Updates

Designers, we really like the design of ameliadrovenko.com(we have attached a picture of the website) , Can we get a homepage like that? so the designs you submit will be 3 pages. The first one should be a page that only has Shop/Look. then the shop page, it should be nothing but our product which we will list the categories ourself. And the look page should contain all the info. such as news, about us and designers etc. Thank you all for your hard work, we really enjoyed the designs. Added Monday, November 03, 2014

Target Market(s)

Our target audiences are woman aged from 16-40 who like online shopping

Industry/Entity Type

Online Shopping

Number of Pages Required

3 page

Font styles to use
Serif
Sans Serif
Script

Requirements
Must have
• Designers,
• we really like the design of ameliadrovenko.com(we have attached a picture of the website) , Can we get a homepage like that? so the designs you submit will be 3 pages. The first one should be a page that only has Shop/Look. then the shop page, it should be nothing but our product which we will list the categories ourself. And the look page should contain all the info. such as news, about us and designers etc. Thank you all for your hard work, we really enjoyed the designs.

```html
<!DOCTYPE html>
<html lang="en">
<head>
<meta charset="utf-8">
<title>QLV Group — The Bright Quarry</title>
<link rel="stylesheet" href="https://fonts.googleapis.com/css2?family=Cormorant+Garamond:wght@500&family=Raleway:wght@300&display=swap">
<style>
  :root {
    --ink-deep: #0b1120;
    --night-blue: #1c2c48;
    --steel-blue: #3b5683;
    --cream: #d9cfc0;
    --card: #ebe9e6;
    --card-text: #3a3a3a;
    --menu-text: #555555;
    --divider: #c9c6c2;
    --brand-red: #c4151c;
  }
  * { margin: 0; padding: 0; box-sizing: border-box; }
  html, body { width: 1200px; height: 781px; overflow: hidden; background: var(--ink-deep); }
  .landing { position: relative; width: 1200px; height: 781px; overflow: hidden; }
  .hero {
    position: absolute; top: 0; height: 781px; width: 600px;
  }
  .hero--print-dress {
    left: 0;
    background:
      radial-gradient(ellipse 180px 320px at 360px 470px, rgba(217,207,192,0.85), rgba(217,207,192,0) 100%),
      radial-gradient(ellipse 120px 160px at 170px 120px, rgba(190,160,140,0.55), rgba(190,160,140,0) 100%),
      linear-gradient(100deg, var(--night-blue) 0%, var(--steel-blue) 30%, var(--ink-deep) 100%);
  }
  .hero--shirt-dress {
    left: 600px;
    background:
      radial-gradient(ellipse 260px 380px at 280px 470px, rgba(93,121,176,0.85), rgba(93,121,176,0) 100%),
      radial-gradient(ellipse 110px 140px at 300px 80px, rgba(190,160,140,0.5), rgba(190,160,140,0) 100%),
      linear-gradient(90deg, var(--ink-deep) 0%, var(--night-blue) 60%, var(--ink-deep) 100%);
  }
  .entry-card {
    position: absolute; left: 460px; top: 183px; width: 281px; height: 419px;
    background: var(--card);
  }
  .entry-card__accent {
    position: absolute; left: 741px; top: 183px; width: 14px; height: 178px;
    background: var(--brand-red);
  }
  .brand {
    position: absolute; top: 80px; left: 0; width: 100%;
    text-align: center; color: var(--card-text);
    font-family: "Cormorant Garamond", Georgia, serif; font-weight: 500;
    font-size: 15.5px; line-height: 15px; letter-spacing: 0.6px;
  }
  .brand__mark {
    display: block; width: 40px; height: 40px; margin: 0 auto 24px;
    border-radius: 50%; background: var(--brand-red);
  }
  .entry-nav { position: absolute; top: 220px; left: 0; width: 100%; }
  .entry-nav__link {
    display: block; height: 69px; line-height: 64px; text-align: center;
    font-family: "Raleway", "Helvetica Neue", Arial, sans-serif; font-weight: 300;
    font-size: 27px; letter-spacing: 9px; padding-left: 9px;
    color: var(--menu-text); text-decoration: none;
  }
  .entry-nav__link--shop { padding-top: 2px; border-bottom: 1px solid var(--divider); }
  .entry-nav__link--look { line-height: 78px; }
</style>
</head>
<body>
  <main class="landing">
    <div class="hero hero--print-dress" role="img" aria-label="Model in a wrapped print dress posing against a glossy dark blue backdrop"></div>
    <div class="hero hero--shirt-dress" role="img" aria-label="Model in a blue brushstroke-print shirt dress posing against a glossy dark blue backdrop"></div>

    <section class="entry-card">
      <div class="brand">
        <span class="brand__mark"></span>
        QLV GROUP<br>THE BRIGHT QUARRY
      </div>
      <nav class="entry-nav">
        <a class="entry-nav__link entry-nav__link--shop" href="#shop">SHOP</a>
        <a class="entry-nav__link entry-nav__link--look" href="#look">LOOK</a>
      </nav>
    </section>
    <div class="entry-card__accent"></div>
  </main>
</body>
</html>
```